parts and kits

we need an updated flyer to email to our customers
we need to have what we sell at kivo
caliper pistons
seal kits
new brake cylinders
brake boosters
brake shoes
brake pads
brake hoses
cables -accelerator, clutch, hand brake etc
for both private, vintage and commercial vehicles

```html
<!DOCTYPE html>
<html lang="en">
<head>
<meta charset="utf-8">
<title>KIVO Auto Centre – Brake &amp; Cable Specialists</title>
<link rel="stylesheet" href="https://fonts.googleapis.com/css2?family=Rubik:wght@500;700;800;900&family=Arimo:wght@400;700&display=swap">
<style>
  :root{
    --ink:#0d0d0f;
    --ink-soft:#18181b;
    --yellow:#e9ea0c;
    --yellow-deep:#d3d30e;
    --yellow-line:#f6f65a;
    --red:#d8261c;
    --white:#ffffff;
    --paper:#f7f7f7;
    --text:#1c1c1c;
    --rule:#9a9a9a;
    --tile-shade:#c9ccd1;
    --tile-dark:#4a4d55;
  }
  *{box-sizing:border-box;margin:0;padding:0}
  html,body{width:710px;height:1200px;overflow:hidden;background:var(--white)}
  .flyer{position:relative;width:710px;height:1200px;background:var(--white);font-family:"Arimo",Arial,sans-serif;color:var(--text)}

  .hero{position:absolute;left:0;top:0;width:710px;height:708px;
    background:radial-gradient(circle at 20% 30%,var(--ink-soft),var(--ink) 60%)}
  .brand{position:absolute;top:38px;width:100%;text-align:center;
    font-family:"Rubik",sans-serif;font-weight:700;font-size:38px;color:var(--yellow);letter-spacing:-.5px}
  .headline{position:absolute;top:92px;width:100%;text-align:center;font-family:"Rubik",sans-serif;font-weight:900;line-height:1}
  .headline .line-one{display:block;color:var(--white);font-size:52px;letter-spacing:-.5px}
  .headline .line-two{display:block;color:var(--red);font-size:72px;margin-top:4px;letter-spacing:-1px}

  .product-grid{position:absolute;left:112px;top:268px;width:486px;display:grid;
    grid-template-columns:repeat(3,138px);column-gap:36px;row-gap:20px}
  .product-tile{height:160px;background:var(--white);border-radius:3px;padding:14px;display:flex}
  .product-photo{flex:1;border-radius:4px;
    background:radial-gradient(ellipse at 50% 50%,var(--tile-dark) 0%,var(--tile-shade) 55%,var(--white) 80%)}

  .parts-tab{position:absolute;left:215px;top:660px;width:280px;height:48px;background:var(--red);
    border-radius:6px 6px 0 0;color:var(--white);font-family:"Rubik",sans-serif;font-weight:700;font-size:27px;
    display:flex;align-items:center;justify-content:center}

  .segments{position:absolute;left:0;top:708px;width:710px;height:176px;display:flex;background:var(--yellow)}
  .segment{display:flex;flex-direction:column;align-items:center;justify-content:flex-end;padding-bottom:26px;
    font-family:"Rubik",sans-serif;font-weight:800;font-size:19px;color:var(--ink)}
  .segment svg{margin-bottom:22px}
  .segment--bikes{width:231px}
  .segment--cars{width:248px;background:var(--yellow-deep);border-left:4px solid var(--yellow-line);border-right:4px solid var(--yellow-line)}
  .segment--commercial{width:231px}

  .info{position:absolute;left:0;top:884px;width:710px;height:276px;
    background:linear-gradient(180deg,var(--white),var(--paper))}
  .about{position:absolute;left:30px;top:40px;width:300px}
  .about h2{font-family:"Rubik",sans-serif;font-weight:800;font-size:19px;color:var(--ink)}
  .about .intro{margin-top:8px;font-size:12px;line-height:1.3}
  .about .intro strong{color:var(--red);font-size:16px;font-weight:700;font-family:"Rubik",sans-serif;font-weight:500}
  .range{list-style:none;margin-top:16px;font-size:12px;line-height:17.5px}
  .range li{position:relative;padding-left:18px}
  .range li::before{content:"";position:absolute;left:1px;top:5px;width:8px;height:8px;border-radius:50%;background:var(--ink)}
  .divider{position:absolute;left:353px;top:36px;width:1px;height:210px;background:var(--rule)}
  .aim{position:absolute;left:401px;top:34px;width:290px}
  .aim h2{font-family:"Rubik",sans-serif;font-weight:900;font-size:38px;color:var(--red);line-height:1}
  .aim p{margin-top:8px;font-size:22px;line-height:1.3;color:var(--text)}

  .base-bar{position:absolute;left:0;bottom:0;width:710px;height:40px;background:var(--ink)}
</style>
</head>
<body>
<main class="flyer">
  <section class="hero">
    <div class="brand">KIVO Auto Centre</div>
    <h1 class="headline">
      <span class="line-one">THE BRAKE &amp; CABLE</span>
      <span class="line-two">SPECIALISTS</span>
    </h1>
    <div class="product-grid">
      <div class="product-tile"><div class="product-photo" role="img" aria-label="Photo of a pair of brake shoes"></div></div>
      <div class="product-tile"><div class="product-photo" role="img" aria-label="Photo of a brake booster with master cylinder"></div></div>
      <div class="product-tile"><div class="product-photo" role="img" aria-label="Photo of a new brake master cylinder"></div></div>
      <div class="product-tile"><div class="product-photo" role="img" aria-label="Photo of a caliper piston"></div></div>
      <div class="product-tile"><div class="product-photo" role="img" aria-label="Photo of a brake pad"></div></div>
      <div class="product-tile"><div class="product-photo" role="img" aria-label="Photo of a brake seal kit"></div></div>
    </div>
    <div class="parts-tab">PARTS FOR</div>
  </section>

  <section class="segments">
    <div class="segment segment--bikes">
      <svg width="78" height="48" viewBox="0 0 78 48" fill="none" stroke="#0d0d0f" stroke-width="3" stroke-linecap="round" stroke-linejoin="round" aria-hidden="true">
        <circle cx="14" cy="34" r="10"/><circle cx="14" cy="34" r="3"/>
        <circle cx="64" cy="34" r="10"/><circle cx="64" cy="34" r="3"/>
        <path d="M14 34h20l10-12h12l8 12"/><path d="M22 22h22l-4 8H24z"/><path d="M52 22l4-12h6"/><path d="M30 16h14"/>
      </svg>
      MOTORBIKES
    </div>
    <div class="segment segment--cars">
      <svg width="60" height="58" viewBox="0 0 60 58" fill="none" stroke="#0d0d0f" stroke-width="3" stroke-linecap="round" stroke-linejoin="round" aria-hidden="true">
        <circle cx="30" cy="16" r="13"/><path d="M24 10l12 12M36 10L24 22"/>
        <path d="M8 38l5-10h6M41 28h6l5 10"/><rect x="5" y="38" width="50" height="12" rx="3"/>
        <path d="M10 50v5h7v-5M43 50v5h7v-5"/><circle cx="13" cy="44" r="2"/><circle cx="47" cy="44" r="2"/><path d="M22 44h16"/>
      </svg>
      CARS
    </div>
    <div class="segment segment--commercial">
      <svg width="76" height="54" viewBox="0 0 76 54" fill="none" stroke="#0d0d0f" stroke-width="3" stroke-linecap="round" stroke-linejoin="round" aria-hidden="true">
        <path d="M8 4h26l4 20"/><path d="M12 4v20M26 4v20"/>
        <path d="M4 24h40l4-6h18l6 12v8h-6"/>
        <circle cx="18" cy="38" r="13"/><circle cx="18" cy="38" r="5"/>
        <circle cx="58" cy="42" r="9"/><circle cx="58" cy="42" r="3"/><path d="M31 40h18"/>
      </svg>
      COMERCIAL
    </div>
  </section>

  <section class="info">
    <div class="about">
      <h2>KIVO AUTO CENTRE</h2>
      <p class="intro"><strong>specialise</strong> in the Re-Manufacture of Brakes,<br>Hoses and Cables</p>
      <ul class="range">
        <li>Brake shoes</li>
        <li>All types of Cables</li>
        <li>Rubber &amp; Braided Hoses</li>
        <li>Difficult to source Brake Parts</li>
        <li>Brake Cylinders, Boosters, Calipers etc..</li>
      </ul>
    </div>
    <div class="divider"></div>
    <div class="aim">
      <h2>OUR AIM</h2>
      <p>is to repair parts with the quickest turn-around times possible</p>
    </div>
  </section>

  <div class="base-bar"></div>
</main>
</body>
</html>
```